Cat-products company needs smart, yet endearing, business card

We need a business card design for a new, but up-and-running, business based in Honolulu, Hawaii. The business is Purrlane Nest Co. Our first product is the most environmentally-friendly cat grass kit ever seen on the planet. Future products, currently in the R&D phase, will include a variety of exciting cat scratchers. We also do consulting work to help apartment-dwellers make their home more cat-friendly and, in the future, plan on doing full, custom installs of structure to create high walkways for cats.

Target Market(s)

Middle-aged, apartment-dwelling, middle-class workers who own 1 or more cats and who dote on them.

Industry/Entity Type

Pet Care

Contact Information for Business Card

A striking, professional, yet warm and friendly design is what we're after.

Font styles to use
Serif
Sans Serif
Other font styles liked:
• Comfortaa

Colors

Designer to choose colors to be used in the design.

Requirements
Must have
• The company logo: (see attachment)
• The company name: Purrlane Nest Co
• The web address: www.purrlanenestco.example
• Email: support@purrlanenestco.example
• Phone: +1 (808) 555 0172
• Update (Fri Jun 30 3017 7:45pm Hawaii Time) I would like, is possible, uploaded picture of the cat grass kit on the back of the card with some text along the lines of: Purrlane Nest Co - Where The Freshest Kitty Sprouts Begin
Nice to have
• A cat picture, cartoon, real or silhouette that illustrates cats in action and/or relaxing; ie using the apartment space to live, play and relax in and being well-contented.
• Most of the website is done in the font: Comfortaa. It might be nice to continue using this for brand consistency.
Should not have
• Hard-to-read fonts.

```html
<!DOCTYPE html>
<html lang="en">
<head>
<meta charset="utf-8">
<title>Purrlane Nest Co — Business Card</title>
<link rel="stylesheet" href="https://fonts.googleapis.com/css2?family=Comfortaa:wght@700&family=Quicksand:wght@500&display=swap">
<style>
  :root {
    --page: #d9d9d9;
    --sky: #b9d1d5;
    --cream: #e9dcbb;
    --cocoa: #58342e;
    --marigold: #fdb400;
    --slate: #6a8f9b;
    --ink: #3b2a26;
  }
  * { box-sizing: border-box; margin: 0; padding: 0; }
  html, body { width: 1200px; height: 876px; overflow: hidden; }
  body {
    background: var(--page);
    display: flex;
    flex-direction: column;
    align-items: center;
    justify-content: center;
    gap: 36px;
    font-family: "Quicksand", sans-serif;
  }
  .card {
    position: relative;
    width: 700px;
    height: 390px;
    overflow: hidden;
    box-shadow: 0 6px 18px rgba(0,0,0,.18);
  }
  .card-front { background: var(--sky); }
  .card-back { background: var(--cream); }
  .edge-band { position: absolute; left: 0; right: 0; bottom: 0; height: 30px; }
  .card-front .edge-band { background: var(--cream); }
  .card-back .edge-band { background: var(--sky); }

  .brand-mark { position: absolute; background: var(--cocoa); border-radius: 6px; }
  .card-front .brand-mark { left: 70px; top: 110px; width: 150px; height: 150px; }
  .card-back .brand-mark { left: 70px; top: 150px; width: 120px; height: 120px; }

  .brand-name {
    font-family: "Comfortaa", sans-serif;
    font-weight: 700;
    color: var(--marigold);
    line-height: 1.05;
  }
  .card-front .brand-name {
    position: absolute; left: 268px; top: 118px;
    display: flex; flex-direction: column; align-items: flex-end;
  }
  .brand-name-main { font-size: 64px; letter-spacing: .5px; }
  .brand-name-sub { font-size: 36px; margin-top: 4px; }

  .front-url {
    position: absolute; left: 0; right: 0; bottom: 42px;
    text-align: center; font-size: 15px; color: var(--ink);
    padding-left: 150px;
  }

  .cat-art {
    position: absolute; right: 110px; top: 18px;
    width: 230px; height: 104px;
    background: var(--cocoa);
    border-radius: 60px 60px 0 0;
  }
  .name-band {
    position: absolute; left: 290px; right: 0; top: 122px; height: 64px;
    background: var(--slate);
    display: flex; align-items: center; justify-content: center;
  }
  .card-back .brand-name { font-size: 34px; }

  .contacts {
    position: absolute; right: 40px; top: 206px;
    list-style: none;
    display: flex; flex-direction: column; gap: 8px;
    font-size: 15px; color: var(--ink);
  }
  .contacts li { display: flex; align-items: center; justify-content: flex-end; gap: 14px; }
  .contacts svg { width: 15px; height: 15px; flex: none; }
</style>
</head>
<body>

<section class="card card-front">
  <div class="brand-mark"></div>
  <h1 class="brand-name">
    <span class="brand-name-main">Purrlane</span>
    <span class="brand-name-sub">Nest Co</span>
  </h1>
  <p class="front-url">www.purrlanenestco.example</p>
  <div class="edge-band"></div>
</section>

<section class="card card-back">
  <div class="brand-mark"></div>
  <div class="cat-art" role="img" aria-label="Illustration of a dark brown cat peeking over the name band"></div>
  <div class="name-band"><h2 class="brand-name">Purrlane Nest Co</h2></div>
  <ul class="contacts">
    <li>+1 (808) 555 0172
      <svg viewBox="0 0 16 16" aria-hidden="true"><path d="M4 1h3l1 4-2 1.5a9 9 0 0 0 3.5 3.5L11 8l4 1v3c0 1-1 2-2 2A12 12 0 0 1 2 3c0-1 1-2 2-2z" fill="var(--cocoa)"/></svg>
    </li>
    <li>support@purrlanenestco.example
      <svg viewBox="0 0 16 16" aria-hidden="true"><rect x="1" y="3" width="14" height="10" fill="var(--cocoa)"/><path d="M1 3l7 6 7-6" fill="none" stroke="var(--cream)" stroke-width="1.2"/></svg>
    </li>
    <li>www.purrlanenestco.example
      <svg viewBox="0 0 16 16" aria-hidden="true"><g fill="none" stroke="var(--cocoa)" stroke-width="1.2"><circle cx="8" cy="8" r="6.5"/><ellipse cx="8" cy="8" rx="3" ry="6.5"/><path d="M1.5 8h13M2.5 4.5h11M2.5 11.5h11"/></g></svg>
    </li>
  </ul>
  <div class="edge-band"></div>
</section>

</body>
</html>
```